Brevv Sauce. Co Label Design Refresh

We need a new label design for an All-Purpose Chili Oil Sauce company based in Southern California. Brevv Sauce is an Asian American family-oriented company. Our sauces are curated in small batches using premium, fresh, sustainable ingredients. All sauces are GF, contain no refined sugars, no msg, no preservatives. Brevv Sauce is not limited, but is great for dipping, topping, marinades, and stir-fry etc. We would like to emphasize that most of our products are Organic, we are currently working on getting all of our products Organic certified. The company is established and is looking to revamp the label. I have attached the following for reference, the redesign brief from our graphic designer who is currently working on revamping our website, Brevv Sauce sales sheet, and the Brevv Sauce website link below,
https://www.brevvsauce.example/

Target Market(s)

Similar target to Green Basket customer. The target customers for Green Basket Grocers are individuals and families whose income is well above the national average, lead a healthy lifestyle and conscious of environment. Most of the customers have college degrees and live in upscale sub-urban or metropolitan areas. Another target group of Green Basket are wealthy customers.

Industry/Entity Type

CPG

Requirements
Must have
• Emphasis on healthiest, natural and organic foods.

```html
<!DOCTYPE html>
<html lang="en">
<head>
<meta charset="UTF-8">
<title>Brevv Sauce – All-Purpose Chili Oil Sauce Label</title>
<link rel="stylesheet" href="https://fonts.googleapis.com/css2?family=Archivo+Black&family=Barlow:wght@500;600;700&family=Barlow+Condensed:wght@600&display=swap">
<style>
  :root {
    --page-bg: #ececec;
    --label-red-light: #b25757;
    --label-red-dark: #8d383d;
    --cream: #f1e4cc;
    --ink: #141111;
  }
  * { margin: 0; padding: 0; box-sizing: border-box; }
  html, body {
    width: 1200px;
    height: 857px;
    overflow: hidden;
    background: var(--page-bg);
  }
  .label {
    position: absolute;
    left: 170px;
    top: 73px;
    width: 860px;
    height: 710px;
    overflow: hidden;
  }
  .label-texture {
    position: absolute;
    inset: 0;
    background: linear-gradient(100deg, var(--label-red-light) 0%, #a44b4e 50%, var(--label-red-dark) 100%);
  }
  .brand {
    position: absolute;
    left: 272px;
    top: 40px;
    width: 316px;
    height: 130px;
    display: flex;
    align-items: center;
    gap: 18px;
  }
  .brand-mark {
    width: 24px;
    height: 24px;
    background: var(--cream);
    flex: none;
  }
  .brand-name {
    font-family: 'Barlow Condensed', sans-serif;
    font-weight: 600;
    font-size: 64px;
    line-height: 0.95;
    color: var(--cream);
    letter-spacing: 1px;
  }
  .centered {
    position: absolute;
    left: 0;
    width: 100%;
    text-align: center;
  }
  .kicker {
    top: 214px;
    font-family: 'Barlow', sans-serif;
    font-weight: 600;
    font-size: 27px;
    letter-spacing: 5px;
    color: var(--cream);
  }
  .product-name {
    font-family: 'Archivo Black', sans-serif;
    color: var(--ink);
    line-height: 1;
    font-size: 132px;
    letter-spacing: -2px;
  }
  .product-name.line-1 { top: 248px; }
  .product-name.line-2 { top: 378px; }
  .rule {
    position: absolute;
    left: 95px;
    width: 640px;
    height: 2px;
    background: var(--cream);
  }
  .rule.top { top: 535px; }
  .rule.bottom { top: 576px; }
  .made-with {
    top: 546px;
    font-family: 'Barlow', sans-serif;
    font-weight: 700;
    font-size: 18px;
    letter-spacing: 3px;
    color: var(--cream);
  }
  .volume {
    position: absolute;
    right: 494px;
    top: 608px;
    text-align: right;
    color: var(--cream);
    font-family: 'Barlow', sans-serif;
  }
  .volume-amount {
    font-weight: 700;
    font-size: 32px;
    line-height: 1;
  }
  .volume-unit {
    font-weight: 500;
    font-size: 17px;
    line-height: 1.2;
  }
  .divider {
    position: absolute;
    left: 403px;
    top: 590px;
    width: 2px;
    height: 101px;
    background: var(--cream);
  }
  .heat-badge {
    position: absolute;
    left: 420px;
    top: 590px;
    width: 202px;
    height: 37px;
    background: var(--ink);
    display: flex;
    align-items: center;
    justify-content: center;
    gap: 14px;
    color: var(--cream);
    font-family: 'Barlow', sans-serif;
    font-weight: 600;
    font-size: 19px;
    letter-spacing: 3px;
  }
  .claims {
    position: absolute;
    left: 429px;
    top: 641px;
    font-family: 'Barlow', sans-serif;
    font-weight: 500;
    font-size: 18px;
    line-height: 23px;
    letter-spacing: 3.5px;
    color: var(--cream);
  }
</style>
</head>
<body>
  <main class="label">
    <div class="label-texture" role="img" aria-label="Red label background with faint topographic contour line pattern"></div>

    <div class="brand">
      <span class="brand-mark"></span>
      <span class="brand-name">BREVV<br>SAUCE</span>
    </div>

    <p class="centered kicker">ALL-PURPOSE</p>
    <h1 class="centered product-name line-1">CHILI OIL</h1>
    <h1 class="centered product-name line-2">SAUCE</h1>

    <div class="rule top"></div>
    <p class="centered made-with">MADE WITH BACON AND SHRIMP</p>
    <div class="rule bottom"></div>

    <div class="volume">
      <p class="volume-amount">7.75 fl. oz.</p>
      <p class="volume-unit">NET WT</p>
    </div>

    <div class="divider"></div>

    <div class="heat-badge">
      <svg width="20" height="18" viewBox="0 0 20 18" aria-hidden="true">
        <path d="M3 2 Q6 9 9 16 L7 16 Q3 9 1 3 Z" fill="var(--cream)"/>
        <path d="M11 2 Q14 9 17 16 L15 16 Q11 9 9 3 Z" fill="var(--cream)"/>
      </svg>
      <span>MEDIUM</span>
    </div>

    <p class="claims">NO MSG<br>GLUTTEN FREE</p>
  </main>
</body>
</html>
```